Brookvale Urgent Care Clinic
Business card and stationary
Brookvale Urgent Care Clinic - Health
Creative Brief
Professional
2847 Quarrow Blvd, Suite 316 Dallas, Texas 75214
wolcastry@mailbrisk.com
www.BrookvaleUC.com
I only want the company name, physicial address and web site on the front with a design. On back only black and white map.
Black and white map of location

```html
<!DOCTYPE html>
<html lang="en">
<head>
<meta charset="utf-8">
<title>Brookvale Urgent Care Clinic – Business Cards</title>
<link rel="stylesheet" href="https://fonts.googleapis.com/css2?family=Cinzel:wght@600&family=Arimo:wght@400&display=swap">
<style>
  :root{
    --stage:#3b3b3d;
    --red:#c4161c;
    --red-dark:#7a0a0e;
    --red-deep:#4a0407;
    --black:#151515;
    --black-soft:#2e2e2e;
    --white:#ffffff;
    --silver:#d6d6d6;
    --ink:#333333;
  }
  *{margin:0;padding:0;box-sizing:border-box}
  html,body{width:1200px;height:691px;overflow:hidden;background:var(--stage)}
  .canvas{position:relative;width:1200px;height:691px}
  .card{position:absolute;border-radius:22px;overflow:hidden;box-shadow:0 6px 18px rgba(0,0,0,.45)}
  .card svg.swoosh{position:absolute;left:0;bottom:0;width:100%;display:block}

  /* front */
  .card-front{left:400px;top:29px;width:570px;height:276px;background:linear-gradient(#ffffff,#f1f1f1)}
  .contact{position:absolute;left:200px;top:26px;font-family:"Arimo",sans-serif;font-size:15px;color:var(--ink);line-height:21px;list-style:none}
  .contact li{display:flex;align-items:center;gap:10px}
  .contact .icon{width:13px;height:13px;flex:none}
  .contact .address{padding-left:23px}
  .brand{position:absolute;display:flex;align-items:center;gap:12px;z-index:2}
  .brand-dot{border-radius:50%;background:radial-gradient(circle at 35% 30%,#ffffff,#bdbdbd);border:3px solid var(--silver);flex:none}
  .brand-name{font-family:"Cinzel",serif;font-weight:600;color:var(--red);line-height:1}
  .brand-name .line1{display:block;font-size:33px;letter-spacing:1px}
  .brand-name .line2{display:block;font-size:13px;letter-spacing:4px;margin-top:5px}
  .card-front .brand{left:40px;top:164px}
  .card-front .brand-dot{width:56px;height:56px}

  /* backs */
  .card-back{top:353px;width:556px;height:307px}
  .card-back.red{left:5px;background:radial-gradient(circle at 55% 40%,var(--red),var(--red-dark) 70%,var(--red-deep))}
  .card-back.black{left:604px;background:radial-gradient(circle at 55% 40%,var(--black-soft),var(--black) 75%)}
  .map{position:absolute;left:20px;top:20px;width:230px;height:200px;border-radius:8px;background:linear-gradient(135deg,rgba(255,255,255,.18),rgba(255,255,255,.05))}
  .card-back .brand-name{position:absolute;left:265px;top:118px;color:var(--white)}
  .card-back .brand-name .line1{font-size:31px}
  .card-back .brand-name .line2{font-size:12px;color:rgba(255,255,255,.8)}
  .card-back .seal{position:absolute;right:26px;bottom:22px;width:66px;height:66px;border-radius:50%;background:radial-gradient(circle at 35% 30%,#ffffff,#bdbdbd);border:4px solid var(--silver)}
</style>
</head>
<body>
<div class="canvas">

  <section class="card card-front">
    <ul class="contact">
      <li class="address">2847 Quarrow Blvd, Suite 316</li>
      <li class="address">Dallas, Texas 75214</li>
      <li><svg class="icon" viewBox="0 0 12 12"><circle cx="6" cy="6" r="6" fill="#c4161c"/><path d="M4 3l1 2-1 1a4 4 0 002 2l1-1 2 1-1 2C5 10 2 7 2 4z" fill="#fff"/></svg>888-555-0147</li>
      <li><svg class="icon" viewBox="0 0 12 12"><circle cx="6" cy="6" r="6" fill="#c4161c"/><rect x="3" y="4" width="6" height="4" fill="#fff"/><path d="M3 4l3 2 3-2" stroke="#c4161c" stroke-width=".8" fill="none"/></svg>wolcastry@mailbrisk.com</li>
      <li><svg class="icon" viewBox="0 0 12 12"><circle cx="6" cy="6" r="6" fill="#c4161c"/><circle cx="6" cy="6" r="3" fill="none" stroke="#fff" stroke-width="1"/><path d="M3 6h6M6 3v6" stroke="#fff" stroke-width=".8"/></svg>www.BrookvaleUC.com</li>
    </ul>
    <svg class="swoosh" viewBox="0 0 570 60" height="60" preserveAspectRatio="none">
      <defs><linearGradient id="fr" x1="0" y1="0" x2="0" y2="1"><stop offset="0" stop-color="#d41d23"/><stop offset="1" stop-color="#7a0a0e"/></linearGradient></defs>
      <path d="M0 14 Q250 56 570 0 L570 10 Q250 66 0 24Z" fill="#cfcfcf"/>
      <path d="M0 24 Q250 66 570 10 L570 60 L0 60Z" fill="url(#fr)"/>
    </svg>
    <div class="brand">
      <span class="brand-dot"></span>
      <span class="brand-name"><span class="line1">BROOKVALE</span><span class="line2">URGENT CARE CLINIC</span></span>
    </div>
  </section>

  <section class="card card-back red">
    <div class="map" role="img" aria-label="Black and white street map of the clinic location"></div>
    <span class="brand-name"><span class="line1">BROOKVALE</span><span class="line2">URGENT CARE CLINIC</span></span>
    <svg class="swoosh" viewBox="0 0 556 90" height="90" preserveAspectRatio="none">
      <path d="M0 60 Q250 10 556 50 L556 58 Q250 22 0 70Z" fill="#e2e2e2"/>
      <path d="M0 70 Q250 22 556 58 L556 90 L0 90Z" fill="rgba(0,0,0,.25)"/>
    </svg>
    <span class="seal"></span>
  </section>

  <section class="card card-back black">
    <div class="map" role="img" aria-label="Black and white street map of the clinic location"></div>
    <span class="brand-name"><span class="line1">BROOKVALE</span><span class="line2">URGENT CARE CLINIC</span></span>
    <svg class="swoosh" viewBox="0 0 556 90" height="90" preserveAspectRatio="none">
      <path d="M0 60 Q250 10 556 50 L556 58 Q250 22 0 70Z" fill="#e2e2e2"/>
      <path d="M0 70 Q250 22 556 58 L556 90 L0 90Z" fill="rgba(0,0,0,.35)"/>
    </svg>
    <span class="seal"></span>
  </section>

</div>
</body>
</html>
```